A4 Folder presentation Design Project

A4 Folder presentation Design.

A4 presentation folder, need to have company logo on it and aligned with company colors

Uploaded my business cards as a reference

Target Market(s)

Business owners

Industry/Entity Type

Electrical

Font styles to use
Sans Serif

Requirements
Must have
• Company logo

Company colors
Orange R:240 G:86 B:47
Blue R:4 G:116 B:187
Dark Grey

```html
<!DOCTYPE html>
<html lang="en">
<head>
<meta charset="utf-8">
<title>Presentation Folder – Apex Electrical Systems</title>
<link href="https://fonts.googleapis.com/css2?family=Montserrat:wght@500;700;800&family=Lato:wght@400&display=swap" rel="stylesheet">
<style>
  :root {
    --orange: #f0562f;
    --blue: #0474bb;
    --grey-light: #e4e4e4;
    --white: #ffffff;
    --navy: #14265c;
  }
  html, body {
    margin: 0;
    padding: 0;
    overflow: hidden;
    background: var(--white);
  }
  .folder {
    position: relative;
    width: 933px;
    height: 1200px;
    overflow: hidden;
    background: var(--white);
    font-family: "Lato", sans-serif;
  }
  .folder__art {
    position: absolute;
    inset: 0;
  }
  .brand {
    position: absolute;
    left: 50px;
    top: 118px;
    display: flex;
    align-items: center;
    gap: 12px;
  }
  .brand__dot {
    width: 26px;
    height: 26px;
    border-radius: 50%;
    background: var(--orange);
  }
  .brand__name {
    font-family: "Montserrat", sans-serif;
    font-weight: 700;
    font-size: 27px;
    letter-spacing: 0.5px;
    color: var(--blue);
    line-height: 1.15;
  }
  .cover-text {
    position: absolute;
    left: 0;
    right: 0;
    top: 960px;
    text-align: center;
    color: var(--white);
  }
  .cover-text__title {
    margin: 0;
    font-family: "Montserrat", sans-serif;
    font-weight: 800;
    font-size: 47px;
    letter-spacing: 0.5px;
  }
  .cover-text__intro {
    margin: 22px auto 0;
    width: 660px;
    font-size: 14.5px;
    line-height: 22px;
  }
  .website {
    position: absolute;
    left: 0;
    right: 0;
    top: 1168px;
    text-align: center;
    color: var(--white);
    font-family: "Montserrat", sans-serif;
    font-weight: 500;
    font-size: 12.5px;
    letter-spacing: 0.3px;
  }
</style>
</head>
<body>
<main class="folder">
  <svg class="folder__art" width="933" height="1200" viewBox="0 0 933 1200" xmlns="http://www.w3.org/2000/svg">
    <defs>
      <linearGradient id="machineTone" x1="0" y1="0" x2="1" y2="1">
        <stop offset="0" stop-color="#6fb0e0"/>
        <stop offset="0.35" stop-color="#2a5ea8"/>
        <stop offset="0.7" stop-color="#1a2f6b"/>
        <stop offset="1" stop-color="#3a4d8c"/>
      </linearGradient>
      <radialGradient id="laserGlow" cx="0.72" cy="0.78" r="0.35">
        <stop offset="0" stop-color="#e0305f" stop-opacity="0.75"/>
        <stop offset="1" stop-color="#e0305f" stop-opacity="0"/>
      </radialGradient>
    </defs>

    <!-- grey swoosh -->
    <path class="wave-grey" fill="var(--grey-light)"
      d="M0 390 C80 350 140 330 220 322 C300 314 350 300 400 250 C450 200 500 160 560 150 L933 150 L933 1200 L0 1200 Z"/>

    <!-- upper orange swoosh -->
    <path class="wave-orange-top" fill="var(--orange)"
      d="M430 230 C470 190 520 160 600 150 C680 142 750 142 800 128 C860 110 900 80 933 30 L933 1200 L430 1200 Z"/>

    <!-- photo area -->
    <g role="img" aria-label="Photo of an automated electronics assembly machine placing components on a circuit board, in blue light with red laser glow">
      <path fill="url(#machineTone)"
        d="M0 406 C60 375 110 360 180 355 C260 350 320 340 380 290 C420 255 450 215 500 200 C570 182 640 190 700 196 C780 204 860 200 933 160 L933 830 L0 880 Z"/>
      <path fill="url(#laserGlow)"
        d="M0 406 C60 375 110 360 180 355 C260 350 320 340 380 290 C420 255 450 215 500 200 C570 182 640 190 700 196 C780 204 860 200 933 160 L933 830 L0 880 Z"/>
    </g>

    <!-- lower orange band -->
    <path class="wave-orange-bottom" fill="var(--orange)"
      d="M0 851 C90 840 170 830 240 805 C310 780 340 735 410 725 C470 718 520 740 580 770 C650 805 720 830 800 830 C860 830 900 820 933 812 L933 1200 L0 1200 Z"/>

    <!-- blue base -->
    <path class="wave-blue" fill="var(--blue)"
      d="M0 872 C100 868 180 855 250 825 C320 795 350 765 410 762 C470 760 520 785 580 810 C650 840 740 860 820 860 C870 860 905 852 933 845 L933 1200 L0 1200 Z"/>
  </svg>

  <div class="brand">
    <span class="brand__dot"></span>
    <span class="brand__name">APEX ELECTRICAL<br>SYSTEMS</span>
  </div>

  <section class="cover-text">
    <h1 class="cover-text__title">PRESENTATION NAME</h1>
    <p class="cover-text__intro">Lorem ipsum dolor sit amet, consectetur adipisicing elit, sed do eiusmod tempor incididunt ut labore et dolore magna aliqua. Ut enim ad minim veniam.</p>
  </section>

  <div class="website">www.apex-brightgrid.com.au</div>
</main>
</body>
</html>
```